New funky, super creative logo design for printing business

Stamp, Wrap and Ship

We are a new digital printing business, based on the Gold Coast of Australia. We have a web site under construction - www.stampwrapandship.net, which will aim at the Business to Business market. We are digital printers, offering a wide variety of print products from business cards to wide format print jobs for consumers and small to medium sized business'. We offer up to date technological, digital and wide format print, at hi octane speed. Our prices are very competitive, and turnaround is super fast.

We like to think outside the box, and this should shine through in the design and colours that you use. Be bold and creative, we want to stand out from the crowd.

We will also soon be needing a full suite of marketing collaterals - posters, letterheads, scrap pads, calendars, banners etc. but this will come later, once we have decided on the logo and layouts.

We want a vibrant, bold image, communicating vibrancy and excitement.

Details on the card are company name: Stamp, Wrap and Ship.
www.stampwrapandship.net.
contact: Marisol (+61)437281956
e-mail:marisol@stampwrapandship.net

I must be able to change some of the details such as the name and number on the card.

Target Market(s)

Business to business, small retail, some individuals

Industry/Entity Type

Construction

Requirements
Must have
• Unique funky logo.
Nice to have
• A three dimensional look,with depth in the logo.

```html
<!DOCTYPE html>
<html lang="en">
<head>
<meta charset="utf-8">
<title>Stamp, Wrap and Ship — Business Card</title>
<link rel="stylesheet" href="https://fonts.googleapis.com/css2?family=Archivo+Black&family=Arimo:wght@700&display=swap">
<style>
  :root {
    --stage: #1c1c1c;
    --card-orange: #f58d1f;
    --white: #ffffff;
    --tagline-purple: #7a4fa0;
    --brand-faint: #c49a63;
    --mark-teal: #2a94c4;
  }
  * { margin: 0; padding: 0; box-sizing: border-box; }
  html, body {
    width: 1200px;
    height: 898px;
    overflow: hidden;
    background: var(--stage);
  }
  .business-card {
    position: absolute;
    left: 42px;
    top: 128px;
    width: 1116px;
    height: 644px;
    background: var(--card-orange);
    font-family: "Arimo", Arial, sans-serif;
    font-weight: 700;
    color: var(--white);
  }
  .brand-lockup {
    position: absolute;
    left: 40px;
    top: 112px;
    display: flex;
    align-items: center;
    gap: 18px;
  }
  .brand-mark {
    width: 44px;
    height: 44px;
    background: var(--mark-teal);
  }
  .brand-name {
    font-family: "Archivo Black", "Arial Black", sans-serif;
    font-weight: 400;
    font-size: 42px;
    color: var(--white);
    white-space: nowrap;
  }
  .tagline {
    position: absolute;
    right: 28px;
    top: 48px;
    font-size: 29px;
    color: var(--tagline-purple);
    transform: rotate(-6deg);
    transform-origin: right center;
    white-space: nowrap;
  }
  .person-name {
    position: absolute;
    left: 0;
    width: 100%;
    top: 304px;
    text-align: center;
    font-size: 32px;
  }
  .contact-block {
    position: absolute;
    right: 28px;
    bottom: 30px;
    text-align: right;
    line-height: 1;
  }
  .brand-echo {
    font-family: "Archivo Black", "Arial Black", sans-serif;
    font-weight: 400;
    font-size: 22px;
    color: var(--brand-faint);
    margin-bottom: 16px;
  }
  .contact-line {
    font-size: 21px;
    margin-top: 9px;
  }
  .website {
    font-size: 25px;
    margin-top: 8px;
    color: var(--white);
  }
</style>
</head>
<body>
  <main class="business-card">
    <div class="brand-lockup">
      <span class="brand-mark"></span>
      <span class="brand-name">Stamp, Wrap and Ship</span>
    </div>

    <p class="tagline">bold print studio</p>

    <h1 class="person-name">Marisol Okafor</h1>

    <div class="contact-block">
      <p class="brand-echo">Stamp, Wrap and Ship</p>
      <p class="contact-line">Telephone: (+61) 437281956</p>
      <p class="contact-line">E-mail: marisol@stampwrapandship.net</p>
      <p class="website">www.stampwrapandship.net</p>
    </div>
  </main>
</body>
</html>
```